Lose Up To 1 LB Of Fat Per Day

We need a double sided street sign for our weight loss clinic. We need the doctors picture to the right side of the sign and we need a challenge “Lose Up To 1 Pound Of Fat Per Day” included in the signage.
Our color scheme for the clinic are black, white, teal and silver.
The phone number should be at the bottom of the sign
555-206–3948

Target Market(s)

Weight Loss

Font styles to use
Sans Serif

```html
<!DOCTYPE html>
<html lang="en">
<head>
<meta charset="utf-8">
<title>Dr. Varlen Weight Loss Program</title>
<link rel="stylesheet" href="https://fonts.googleapis.com/css2?family=PT+Sans:ital,wght@0,700;1,700&display=swap">
<style>
  :root {
    --ink: #050505;
    --paper: #ffffff;
    --slate: #58585a;
    --navy: #28306a;
    --shadow-grey: #b9b9bb;
    --photo-light: #d9dadf;
    --photo-mid: #b9bccb;
    --photo-coat: #a9b3dc;
  }
  * { margin: 0; padding: 0; box-sizing: border-box; }
  html, body { width: 1200px; height: 384px; overflow: hidden; background: var(--paper); }
  .sign {
    position: relative;
    width: 1200px;
    height: 384px;
    background: var(--paper);
    font-family: "PT Sans", Arial, sans-serif;
    overflow: hidden;
  }
  .sign__shapes { position: absolute; inset: 0; }
  .tag {
    position: absolute;
    top: 49px;
    height: 43px;
    color: var(--paper);
    font-weight: 700;
    display: flex;
    align-items: center;
    white-space: nowrap;
  }
  .tag--name { left: 418px; font-size: 29px; }
  .tag--program { left: 642px; font-size: 22px; letter-spacing: 0.2px; }
  .headline {
    position: absolute;
    left: 446px;
    top: 118px;
    color: var(--ink);
    font-style: italic;
    font-weight: 700;
    font-size: 75px;
    line-height: 79px;
    letter-spacing: -0.5px;
    text-shadow: 4px 3px 0 var(--shadow-grey);
    white-space: nowrap;
  }
  .phone {
    position: absolute;
    left: 440px;
    top: 281px;
    height: 67px;
    display: flex;
    align-items: center;
    color: var(--paper);
    font-weight: 700;
    font-size: 62px;
    letter-spacing: 0.5px;
    white-space: nowrap;
  }
</style>
</head>
<body>
<div class="sign">
  <svg class="sign__shapes" width="1200" height="384" viewBox="0 0 1200 384" aria-hidden="false">
    <defs>
      <linearGradient id="portraitTone" x1="0" y1="0" x2="0.6" y2="1">
        <stop offset="0" stop-color="var(--photo-light)"/>
        <stop offset="0.55" stop-color="var(--photo-mid)"/>
        <stop offset="1" stop-color="var(--photo-coat)"/>
      </linearGradient>
    </defs>
    <polygon class="portrait" role="img" aria-label="Portrait of the doctor in a white coat with a stethoscope, arms crossed" points="0,0 380,0 320,384 0,384" fill="url(#portraitTone)"/>
    <polygon class="divider-band" points="388,0 455,0 395,384 328,384" fill="var(--ink)"/>
    <polygon class="tag-plate" points="407,49 612,49 603,92 399,92" fill="var(--slate)"/>
    <polygon class="tag-plate" points="617,49 966,49 952,92 605,92" fill="var(--slate)"/>
    <rect class="rule" x="441" y="99" width="677" height="2.5" fill="var(--navy)"/>
    <path class="phone-bar" d="M359,283 H1020 A32.5,32.5 0 0 1 1020,348 H359 Z" fill="var(--slate)"/>
  </svg>

  <div class="tag tag--name">DR. VARLEN</div>
  <div class="tag tag--program">WEIGHT LOSS PROGRAM</div>

  <h1 class="headline">LOSE UP TO 1 POUND<br>OF FAT PER DAY</h1>

  <div class="phone">(555)-206–3948</div>
</div>
</body>
</html>
```